homepage design , industry automation control image

we need a design , based on our Logo image.

we focus on selling of temprature sensor ,and parts.

but need concept or image on industry automation control

we need enviroment friendly concept.

Industry/Entity Type

Industry

Number of Pages Required

5+ page

Requirements
Must have
• we need a Cartoon Image of a Temperature sensor,
• attaching a Excel file with the sensor looking.
Nice to have
• Nature image, future concept

```html
<!DOCTYPE html>
<html lang="en">
<head>
<meta charset="utf-8">
<title>Kessler Sensorik – Home</title>
<link href="https://fonts.googleapis.com/css2?family=Nunito:wght@400;600;700&family=Open+Sans:wght@400;600&display=swap" rel="stylesheet">
<style>
:root{
  --green:#1f8a1f;
  --green-band:#217f22;
  --green-light:#5cc02c;
  --ink:#1e1e1e;
  --text:#444;
  --muted:#8a8a8a;
  --grey-bg:#f2f2f2;
  --footer-bg:#f4f4f4;
  --white:#fff;
}
*{box-sizing:border-box;margin:0;padding:0}
html,body{width:1200px;height:2449px;overflow:hidden;background:var(--white)}
body{position:relative;font-family:"Open Sans",Arial,sans-serif;color:var(--text)}
h1,h2,h3,h4{font-weight:400}
.abs{position:absolute}

/* header */
.site-header{left:0;top:0;width:1200px;height:98px;background:var(--white)}
.brand{display:flex;align-items:center;gap:8px;font-family:"Nunito",Arial,sans-serif;font-weight:700;color:var(--green);white-space:nowrap}
.brand-mark{width:44px;height:44px;background:var(--green);border:3px solid var(--green-light)}
.site-header .brand{position:absolute;left:93px;top:27px;font-size:27px}
.main-nav{font-family:"Nunito",Arial,sans-serif;font-size:15px;color:var(--ink)}
.main-nav a{position:absolute;top:44px;color:inherit;text-decoration:none;white-space:nowrap;line-height:18px}
.main-nav a.active{top:36px;width:77px;height:36px;line-height:33px;text-align:center;border:1.5px solid var(--green);border-radius:20px;color:var(--green)}

/* hero */
.hero{left:0;top:98px;width:1200px;height:490px;background:linear-gradient(180deg,#9fb6c9 0%,#c9d3d6 30%,#a08a6a 55%,#7a6a4e 80%,#5e5a4c 100%)}
.hero-title{position:absolute;left:0;width:100%;top:226px;text-align:center;font-family:"Open Sans",Arial,sans-serif;font-weight:600;font-size:55px;color:var(--white);letter-spacing:.5px}
.hero-arrow{position:absolute;top:412px;width:22px;height:22px}

/* welcome band */
.welcome{left:0;top:588px;width:1200px;height:201px;background:var(--green-band);color:var(--white);text-align:center}
.welcome h1{font-family:"Nunito",Arial,sans-serif;font-size:30px;margin-top:44px;letter-spacing:.3px}
.welcome p{width:830px;margin:16px auto 0;font-size:14.6px;line-height:24px}

/* products */
.section-title{left:0;width:1200px;text-align:center;font-family:"Nunito",Arial,sans-serif;font-size:30px;color:var(--ink)}
.section-sub{left:0;width:1200px;text-align:center;font-size:17.5px;color:var(--muted)}
.product{width:300px;text-align:center}
.product-icon{width:98px;height:98px;margin:0 auto;border:3px solid var(--green-light);padding:4px;background:var(--white)}
.product-icon div{width:100%;height:100%;background:var(--green);display:flex;align-items:center;justify-content:center}
.product h3{font-family:"Nunito",Arial,sans-serif;font-size:17px;color:var(--ink);margin-top:26px;letter-spacing:.3px}
.product p{font-size:12.8px;line-height:20px;color:var(--muted);margin-top:12px;padding:0 22px}
.product .more{display:block;font-size:13px;color:var(--ink);margin-top:10px}

/* automation */
.automation-photo{left:0;top:1334px;width:577px;height:348px;background:linear-gradient(180deg,#6f8fb3 0%,#8ea9c4 25%,#55704e 55%,#3f5a3a 100%)}
.automation-panel{left:577px;top:1334px;width:623px;height:348px;background:var(--grey-bg)}
.automation-panel h2{position:absolute;left:42px;top:70px;font-family:"Nunito",Arial,sans-serif;font-size:31px;color:var(--green)}
.automation-panel p{position:absolute;left:39px;top:116px;width:494px;font-size:14.6px;line-height:24.5px;text-align:justify;hyphens:auto;color:var(--text)}

/* blog & reviews */
.block-title{font-family:"Nunito",Arial,sans-serif;font-size:20px;color:var(--ink)}
.post{left:95px;width:560px;height:118px}
.post-photo{position:absolute;left:0;top:0;width:179px;height:118px;border:3px solid #fff;box-shadow:0 0 4px rgba(0,0,0,.3)}
.post-body{position:absolute;left:205px;top:10px;width:350px}
.post-body h4{font-family:"Nunito",Arial,sans-serif;font-weight:600;font-size:13.5px;color:var(--ink)}
.post-body .date{font-size:10.5px;color:var(--ink);margin-top:8px}
.post-body p{font-size:11px;line-height:18px;color:var(--text);margin-top:6px}
.post-body .read{font-size:10px;color:var(--green);margin-top:6px;display:block}
.review-card{left:779px;top:1829px;width:333px;height:155px;background:var(--green);color:var(--white);padding:22px 18px;font-size:11.5px;line-height:25px;border-radius:2px}
.quote{font-family:Georgia,serif;font-weight:700;font-size:24px;line-height:10px;vertical-align:-6px}
.avatar{left:801px;top:2001px;width:80px;height:80px;border-radius:50%;background:radial-gradient(circle at 50% 45%,#d7b49a,#8a6e5b)}
.reviewer{left:897px;top:2008px;font-family:"Nunito",Arial,sans-serif;font-size:15.5px;color:var(--ink)}
.pager{top:2053px;width:22px;height:22px;border-radius:3px;background:#f0f0f0}

/* footer */
.site-footer{left:0;top:2169px;width:1200px;height:207px;background:var(--footer-bg);border-bottom:1px solid #e2e2e2}
.footer-map{left:88px;top:2198px;width:248px;height:137px;background:linear-gradient(135deg,#e9e7df 0%,#dcdfd2 45%,#b9d3ea 60%,#e6e4dc 100%)}
.site-footer .brand{position:absolute;left:377px;top:44px;font-size:18px;gap:6px}
.site-footer .brand-mark{width:32px;height:32px;border-width:2px}
.contact{position:absolute;left:377px;font-size:11px;color:var(--text);display:flex;align-items:center;gap:8px;white-space:nowrap}
.footer-head{font-family:"Nunito",Arial,sans-serif;font-size:14px;color:var(--ink)}
.links{position:absolute;left:706px;top:92px;list-style:none;font-size:10.5px;line-height:21.5px;color:var(--text)}
.links li::before{content:"▸";font-size:8px;margin-right:5px;color:#666}
.newsletter{position:absolute;left:870px;top:91px;display:flex}
.newsletter span{width:183px;height:31px;border:1px solid #ccc;background:#fff;font-size:11px;padding:7px 12px;color:#666}
.newsletter b{width:57px;height:31px;background:var(--green);color:#fff;font-weight:400;font-size:11.5px;display:flex;align-items:center;justify-content:center}
.social{position:absolute;left:877px;top:141px;display:flex;gap:14px}
.social i{width:21px;height:21px;border-radius:3px;background:#2b2b2b;display:block}
.copyright{left:0;top:2406px;width:1200px;text-align:center;font-size:13px;color:var(--ink)}
</style>
</head>
<body>

<header class="abs site-header">
  <div class="brand"><span class="brand-mark"></span>Kessler Sensorik</div>
  <nav class="main-nav">
    <a class="active" style="left:472px">HOME</a>
    <a style="left:560px">ABOUT US</a>
    <a style="left:661px">SERVICES</a>
    <a style="left:758px">PRODUCTS</a>
    <a style="left:862px">SUPPORTS</a>
    <a style="left:967px">BLOG</a>
    <a style="left:1029px">CONTACTS</a>
  </nav>
</header>

<section class="abs hero" role="img" aria-label="City skyline with cathedral towers, a river bridge and trees in autumn colours">
  <div class="hero-title">KESSLER SENSORIK</div>
  <svg class="hero-arrow" style="left:93px" viewBox="0 0 22 22"><path d="M13 5 7 11l6 6" fill="none" stroke="#fff" stroke-width="2"/></svg>
  <svg class="hero-arrow" style="left:126px" viewBox="0 0 22 22"><path d="M9 5l6 6-6 6" fill="none" stroke="#fff" stroke-width="2"/></svg>
</section>

<section class="abs welcome">
  <h1>WELCOME TO KESSLER SENSORIK</h1>
  <p>It has survived not only five centuries, but also the leap into electronic typesetting, remaining essentially unchanged. It was popularised in the 1960s with the release of Typexa sheets containing Lorem Ipsum passages, and more recently with desktop publishing software like Folio PageCrafter including versions of Lorem Ipsu</p>
</section>

<h2 class="abs section-title" style="top:866px">OUR PRODUCTS</h2>
<p class="abs section-sub" style="top:913px">porro quisquam est qui dolorem</p>

<article class="abs product" style="left:119px;top:990px">
  <div class="product-icon"><div>
    <svg width="44" height="60" viewBox="0 0 44 60" fill="none" stroke="#fff" stroke-width="3"><rect x="14" y="4" width="12" height="36" rx="6"/><circle cx="20" cy="46" r="9"/><line x1="20" y1="20" x2="20" y2="44"/><line x1="31" y1="10" x2="38" y2="10"/><line x1="31" y1="17" x2="36" y2="17"/><line x1="31" y1="24" x2="38" y2="24"/></svg>
  </div></div>
  <h3>TEMPERATURE SENSOR</h3>
  <p>It has survived not only five centuries, but also the leap into electronic typesetting, remaining essentially unchanged.</p>
  <span class="more">Learn More -&gt;</span>
</article>

<article class="abs product" style="left:449px;top:990px">
  <div class="product-icon"><div>
    <svg width="60" height="60" viewBox="0 0 60 60" fill="none" stroke="#fff" stroke-width="3"><rect x="26" y="8" width="10" height="30" rx="5"/><circle cx="31" cy="44" r="8"/><circle cx="17" cy="30" r="7"/><line x1="17" y1="17" x2="17" y2="21"/><line x1="6" y1="30" x2="9" y2="30"/><line x1="9" y1="21" x2="11" y2="24"/><line x1="9" y1="39" x2="11" y2="36"/><line x1="41" y1="14" x2="48" y2="14"/><line x1="41" y1="22" x2="46" y2="22"/><line x1="41" y1="30" x2="48" y2="30"/></svg>
  </div></div>
  <h3>TEMPERATURE SENSOR PARTS</h3>
  <p>It has survived not only five centuries, but also the leap into electronic typesetting, remaining essentially unchanged.</p>
  <span class="more">Learn More -&gt;</span>
</article>

<article class="abs product" style="left:776px;top:990px">
  <div class="product-icon"><div>
    <svg width="60" height="60" viewBox="0 0 60 60" fill="none" stroke="#fff" stroke-width="3"><rect x="10" y="12" width="7" height="36" rx="3"/><rect x="20" y="12" width="7" height="36" rx="3"/><rect x="30" y="12" width="7" height="36" rx="3"/><rect x="40" y="12" width="7" height="36" rx="3"/><line x1="4" y1="22" x2="53" y2="22"/><line x1="4" y1="40" x2="53" y2="40"/></svg>
  </div></div>
  <h3>HEATER &amp; PARTS</h3>
  <p>It has survived not only five centuries, but also the leap into electronic typesetting, remaining essentially unchanged.</p>
  <span class="more">Learn More -&gt;</span>
</article>

<div class="abs automation-photo" role="img" aria-label="Office tower rising above a green landscape under a blue sky"></div>
<section class="abs automation-panel" lang="en">
  <h2>INDUSTRY AUTOMATION</h2>
  <p>It is a long established fact that a reader will be distracted by the readable content of a page when looking at its layout. The point of using Lorem Ipsum is that it has a more-or-less normal distribution of letters, as opposed to using 'Content here, content here', making it look like readable English. Many desktop publishing packages and web page editors now use Lorem Ipsum as their default model text, and a search for 'lorem ipsum' will uncover many web sites still in their infancy.</p>
</section>

<h3 class="abs block-title" style="left:93px;top:1784px">LATEST BLOG</h3>

<article class="abs post" style="top:1829px">
  <div class="post-photo" role="img" aria-label="Sunlit forest with green trees" style="background:linear-gradient(160deg,#cfe3f0 0%,#7fb24a 45%,#3f7a2a 100%)"></div>
  <div class="post-body">
    <h4>Nemo Enim Ipsam Voluptatem</h4>
    <div class="date">JULY 20, 2017</div>
    <p>Lorem ipsum dolor sit amet, consectetur adipiscing elit, sed do eiusmod tempor incididunt ut labore</p>
    <span class="read">Read More »</span>
  </div>
</article>

<article class="abs post" style="top:1970px">
  <div class="post-photo" role="img" aria-label="Small tree growing from soil held in open hands" style="background:linear-gradient(160deg,#eef0ea 0%,#a9c489 50%,#6e8f52 100%)"></div>
  <div class="post-body">
    <h4>Nemo Enim Ipsam Voluptatem</h4>
    <div class="date">JULY 20, 2017</div>
    <p>Lorem ipsum dolor sit amet, consectetur adipiscing elit, sed do eiusmod tempor incididunt ut labore</p>
    <span class="read">Read More »</span>
  </div>
</article>

<h3 class="abs block-title" style="left:774px;top:1784px">REVIEWS</h3>
<blockquote class="abs review-card"><span class="quote">“</span> Lorem Ipsum has been the industry's standard dummy text ever since the 1500s, when an unknown printer took a galley of type and scrambled it to make a type specimen book. It has survived only five <span class="quote">”</span></blockquote>
<div class="abs avatar" role="img" aria-label="Portrait photo of the reviewer"></div>
<div class="abs reviewer">Jonas Berg - Manager</div>
<svg class="abs pager" style="left:899px" viewBox="0 0 22 22"><path d="M13 7l-4 4 4 4" fill="none" stroke="#555" stroke-width="1.5"/></svg>
<svg class="abs pager" style="left:925px" viewBox="0 0 22 22"><path d="M9 7l4 4-4 4" fill="none" stroke="#555" stroke-width="1.5"/></svg>

<footer class="abs site-footer">
  <div class="brand"><span class="brand-mark"></span>Kessler Sensorik</div>
  <div class="contact" style="top:89px"><svg width="10" height="12" viewBox="0 0 10 12"><path d="M5 12S0 6.5 0 4a5 5 0 0110 0c0 2.5-5 8-5 8z" fill="var(--green)"/><circle cx="5" cy="4" r="1.7" fill="#fff"/></svg>12 Brookfield Lane, Millbay, Avonford AV3 7QK</div>
  <div class="contact" style="top:115px"><svg width="11" height="11" viewBox="0 0 11 11"><path d="M2 0l2 3-1.2 1.3a7 7 0 003.9 3.9L8 7l3 2-1 2C4.5 11 0 6.5 0 1z" fill="var(--green)"/></svg>314-555-0142.</div>
  <div class="contact" style="top:141px"><svg width="12" height="9" viewBox="0 0 12 9"><rect width="12" height="9" fill="var(--green)"/><path d="M0 0l6 5 6-5" fill="none" stroke="#fff" stroke-width="1"/></svg>Email : info@kesslersensorik.example</div>
  <div class="footer-head abs" style="left:704px;top:50px">LINKS</div>
  <ul class="links"><li>ABOUT US</li><li>SERVICES</li><li>SUPPORT</li><li>NEWS</li></ul>
  <div class="footer-head abs" style="left:870px;top:50px">SIGN UP FOR NEWSLETTER</div>
  <div class="newsletter"><span>Email address</span><b>Submit</b></div>
  <div class="social"><i></i><i></i><i></i><i></i></div>
</footer>
<div class="abs footer-map" role="img" aria-label="Street map of the city with a river and a location pin"></div>

<p class="abs copyright">Copyright © 2017. All Rights Reserved</p>

</body>
</html>
```